Business Card Design Project

I have attached the logo and the colour pallete for the branding for the company.

Creative designs for business cards are needed.

The Company is modern corporate.

Industry/Entity Type

Business

```html
<!DOCTYPE html>
<html lang="en">
<head>
<meta charset="utf-8">
<title>Northvale Business Card</title>
<link rel="stylesheet" href="https://fonts.googleapis.com/css2?family=Noto+Serif:wght@700&display=swap">
<style>
  :root {
    --backdrop: #e9e7ec;
    --plum-deep: #22062f;
    --plum-mid: #3a0f4d;
    --plum-glow: #b9a3cc;
    --card-grey: #cdcbd0;
    --mark-lilac: #b2a4bd;
    --ink-plum: #2c0b4a;
    --accent-orange: #f0561c;
    --wordmark-dark: #151018;
  }
  html, body {
    margin: 0;
    padding: 0;
    width: 1200px;
    height: 960px;
    overflow: hidden;
    background: var(--backdrop);
  }
  .sheet {
    width: 1200px;
    height: 960px;
    display: flex;
    align-items: center;
    justify-content: center;
    gap: 48px;
    font-family: "Noto Serif", Georgia, serif;
    font-weight: 700;
  }
  .card {
    width: 540px;
    height: 340px;
    position: relative;
    overflow: hidden;
    box-shadow: 0 6px 18px rgba(0,0,0,0.18);
  }
  /* Front side */
  .card--front {
    background: radial-gradient(ellipse 46% 44% at 50% 50%, var(--plum-glow) 0%, #7b5b93 22%, var(--plum-mid) 55%, var(--plum-deep) 100%);
  }
  .front-wordmark {
    position: absolute;
    left: 0;
    right: 0;
    top: 138px;
    text-align: center;
    font-size: 46px;
    line-height: 1.1;
    letter-spacing: 1px;
    color: var(--wordmark-dark);
  }
  .front-flare {
    position: absolute;
    left: 90px;
    right: 90px;
    top: 196px;
    height: 3px;
    background: linear-gradient(90deg, transparent, rgba(255,255,255,0.9), transparent);
  }
  /* Back side */
  .card--back {
    background: var(--card-grey);
  }
  .back-wordmark {
    position: absolute;
    left: 26px;
    top: 22px;
    font-size: 92px;
    line-height: 1;
    color: var(--mark-lilac);
  }
  .holder {
    position: absolute;
    right: 28px;
    top: 176px;
    display: flex;
    align-items: baseline;
    gap: 18px;
  }
  .holder-name {
    font-size: 21px;
    color: var(--ink-plum);
  }
  .holder-role {
    width: 62px;
    font-size: 15px;
    color: var(--accent-orange);
  }
  .contact-list {
    position: absolute;
    right: 28px;
    top: 232px;
    margin: 0;
    padding: 0;
    list-style: none;
  }
  .contact-row {
    display: flex;
    justify-content: flex-end;
    align-items: baseline;
    gap: 18px;
    margin-bottom: 6px;
  }
  .contact-value {
    text-align: right;
    font-size: 14px;
    color: var(--ink-plum);
    white-space: nowrap;
  }
  .contact-label {
    width: 62px;
    font-size: 11px;
    color: var(--accent-orange);
  }
</style>
</head>
<body>
  <main class="sheet">
    <section class="card card--front" aria-label="Card front">
      <div class="front-wordmark">northvale</div>
      <div class="front-flare"></div>
    </section>

    <section class="card card--back" aria-label="Card back">
      <div class="back-wordmark">northvale</div>
      <div class="holder">
        <span class="holder-name">Daniel Reyes Amador</span>
        <span class="holder-role">CEO</span>
      </div>
      <ul class="contact-list">
        <li class="contact-row">
          <span class="contact-value">01 555 0142</span>
          <span class="contact-label">Contact</span>
        </li>
        <li class="contact-row">
          <span class="contact-value">daniel_reyes@northvale.net</span>
          <span class="contact-label">e mail</span>
        </li>
        <li class="contact-row">
          <span class="contact-value">northvale.net</span>
          <span class="contact-label">website</span>
        </li>
      </ul>
    </section>
  </main>
</body>
</html>
```